Everything fresh, everything new

When I take over the practice, I would like to breathe new life into the practice. I want a business card design that catches the eye and brings a breath of fresh air

```html
<!DOCTYPE html>
<html lang="de">
<head>
<meta charset="utf-8">
<title>Praxisfeld – Visitenkarte</title>
<link rel="stylesheet" href="https://fonts.googleapis.com/css2?family=Montserrat:wght@400;500;700&display=swap">
<style>
  :root {
    --stage: #1c1c1d;
    --card-dark: #4b4b4c;
    --card-light: #ffffff;
    --ink: #3c3c3e;
    --silver: #c9c9cb;
    --green: #8cc63f;
    --rule: #3c3c3e;
  }
  * { box-sizing: border-box; margin: 0; padding: 0; }
  html, body { width: 1200px; height: 875px; overflow: hidden; }
  body {
    background: var(--stage);
    font-family: "Montserrat", sans-serif;
    color: var(--ink);
    position: relative;
  }
  .card {
    position: absolute;
    top: 282px;
    width: 540px;
    height: 310px;
    border-radius: 18px;
  }
  .card--front { left: 40px; background: var(--card-dark); }
  .card--back  { left: 620px; background: var(--card-light); }

  .brand {
    position: absolute;
    display: flex;
    align-items: center;
    gap: 10px;
    font-weight: 500;
    letter-spacing: 0.5px;
  }
  .brand__ring { flex: none; }
  .card--front .brand {
    left: 50%; top: 50%;
    transform: translate(-50%, -50%);
    font-size: 46px;
    color: var(--silver);
  }
  .card--back .brand {
    right: 34px; top: 38px;
    font-size: 28px;
    color: var(--ink);
  }

  .person { position: absolute; left: 34px; top: 150px; }
  .person__name {
    font-size: 27px; font-weight: 700; letter-spacing: 1px;
    text-transform: uppercase;
  }
  .person__role {
    margin-top: 4px;
    font-size: 15px; font-weight: 400; letter-spacing: 0.5px;
    text-transform: uppercase;
  }

  .divider {
    position: absolute; left: 34px; right: 34px; top: 222px;
    height: 1.5px; background: var(--rule);
  }

  .contacts {
    position: absolute; left: 34px; right: 34px; top: 236px;
    display: flex; justify-content: space-between;
    font-size: 13px; line-height: 22px;
  }
  .contact-list { list-style: none; }
  .contact-list li { display: flex; align-items: center; gap: 7px; }
  .contact-list svg { flex: none; }
  .address { font-style: normal; text-align: right; }
</style>
</head>
<body>

<section class="card card--front" aria-label="Vorderseite">
  <div class="brand">
    <svg class="brand__ring" width="26" height="26" viewBox="0 0 26 26" aria-hidden="true">
      <circle cx="13" cy="13" r="10" fill="none" stroke="var(--silver)" stroke-width="3"/>
    </svg>
    <span>Praxisfeld</span>
  </div>
</section>

<section class="card card--back" aria-label="Rückseite">
  <div class="brand">
    <svg class="brand__ring" width="22" height="22" viewBox="0 0 22 22" aria-hidden="true">
      <circle cx="11" cy="11" r="8.5" fill="none" stroke="var(--green)" stroke-width="2.5"/>
    </svg>
    <span>Praxisfeld</span>
  </div>

  <div class="person">
    <p class="person__name">Lukas Brenner</p>
    <p class="person__role">Managing Director</p>
  </div>

  <div class="divider"></div>

  <div class="contacts">
    <ul class="contact-list">
      <li>
        <svg width="10" height="14" viewBox="0 0 10 14" aria-hidden="true"><rect x="1" y="0.75" width="8" height="12.5" rx="1.5" fill="none" stroke="var(--green)" stroke-width="1.5"/><circle cx="5" cy="10.5" r="0.9" fill="var(--green)"/></svg>
        044-987 650 112
      </li>
      <li>
        <svg width="12" height="12" viewBox="0 0 12 12" aria-hidden="true"><path d="M2.5 1l2 2.5-1.2 1.2a7 7 0 0 0 4 4L8.5 7.5 11 9.5l-1.3 1.7C5.5 11 1 6.5.8 2.3z" fill="var(--green)"/></svg>
        044-987 650 113
      </li>
    </ul>
    <ul class="contact-list">
      <li>
        <svg width="13" height="10" viewBox="0 0 13 10" aria-hidden="true"><rect x="0.5" y="0.5" width="12" height="9" fill="var(--green)"/><path d="M0.5 0.5l6 5 6-5" fill="none" stroke="#fff" stroke-width="1"/></svg>
        hallo@praxisfeld.example
      </li>
      <li>
        <svg width="12" height="12" viewBox="0 0 12 12" aria-hidden="true"><circle cx="6" cy="6" r="5.5" fill="var(--green)"/><path d="M0.5 6h11M6 .5c-3 3-3 8 0 11M6 .5c3 3 3 8 0 11" fill="none" stroke="#fff" stroke-width="0.8"/></svg>
        www.praxisfeld.example
      </li>
    </ul>
    <address class="address">
      18, Lindenweg Süd<br>Ortsmitte 80331,
    </address>
  </div>
</section>

</body>
</html>
```